Business card for Eyelash extension salon in Beverly Hills,California USA

We need new business card for our salon in Beverly Hills. The salon name is 'Lumarra' . We would like to have...Business name: Lumarra Name of person: will provide later Address 6128 N.Corbel Ridge Blvd Beverly Hills , CA 90210 Phone: will provide later (Text only) Web: www.lumarrastudio-example.com Pictogrid icon, Friendvale icon follow us for seasonal campaign and news @lumarrastudioexample Design should look elegant, high-end, clean, simple, cohesive with my brand. Please refer my brand board. Business name color will be metallic bronzy color. Im thinking grey background or white background. Thanks

Target Market(s)

25-35. Gender neutral. People who are in Entertainment business industry.
This is High-end Eyelash extension salon in Beverly Hills

Industry/Entity Type

Beauty Salon

Contact Information for Business Card

Business name: Lumarra
Name of person: will provide later
Address 6128 N.Corbel Ridge Blvd Beverly Hills , CA 90210
Phone: will provide later (Text only)
Web: www.lumarrastudio-example.com
Pictogrid icon, Friendvale icon
follow us for seasonal campaign and news @lumarrastudioexample

Requirements
Must have
• Beautiful, elegant, clean and simple look but very attractive and modern
Should not have
• We don't like too clutter, too busy designs.

```html
<!DOCTYPE html>
<html lang="en">
<head>
<meta charset="utf-8">
<title>Lumarra Business Card</title>
<link rel="stylesheet" href="https://fonts.googleapis.com/css2?family=Arimo:wght@400;700&family=Tinos:wght@700&display=swap">
<style>
  :root {
    --backdrop: #e6e6e3;
    --card: #fbfbf9;
    --bronze: #a27d4e;
    --ink: #2b2b2b;
    --rule: #a98a62;
  }
  * { box-sizing: border-box; margin: 0; padding: 0; }
  html, body { width: 1200px; height: 800px; overflow: hidden; }
  body {
    background: var(--backdrop);
    font-family: "Arimo", Arial, sans-serif;
    display: flex;
    align-items: center;
    justify-content: center;
    gap: 40px;
  }
  .card {
    width: 540px;
    height: 309px;
    background: var(--card);
    box-shadow: 0 2px 6px rgba(0,0,0,0.08);
    position: relative;
  }
  /* Front */
  .card--front {
    display: flex;
    align-items: center;
    justify-content: center;
  }
  .brand {
    display: flex;
    flex-direction: column;
    align-items: flex-end;
    color: var(--bronze);
  }
  .brand__name {
    font-family: "Arimo", Arial, sans-serif;
    font-weight: 400;
    font-size: 64px;
    letter-spacing: 1px;
    line-height: 1;
  }
  .brand__place {
    font-size: 10px;
    letter-spacing: 3px;
    margin-top: 8px;
  }
  .card--back .brand {
    position: absolute;
    top: 48px;
    right: 44px;
  }
  .card--back .brand__name { font-size: 40px; }
  .card--back .brand__place { font-size: 7px; letter-spacing: 2px; margin-top: 5px; }

  /* Back */
  .person {
    position: absolute;
    left: 30px;
    right: 30px;
    top: 170px;
  }
  .person__row {
    display: flex;
    align-items: center;
    gap: 14px;
  }
  .person__name {
    font-family: "Tinos", "Times New Roman", serif;
    font-weight: 700;
    font-size: 19px;
    color: var(--bronze);
    white-space: nowrap;
  }
  .rule { flex: 1; height: 1px; background: var(--rule); }
  .person__role {
    font-size: 13px;
    color: var(--ink);
    margin-top: 4px;
  }
  .rule--full { margin-top: 12px; }
  .contact {
    list-style: none;
    margin-top: 12px;
    font-size: 12px;
    color: var(--ink);
    line-height: 1.75;
    letter-spacing: 0.3px;
  }
  .contact__label { color: var(--bronze); font-weight: 700; margin-right: 4px; }
  .contact__item + .contact__label { margin-left: 8px; }
</style>
</head>
<body>
  <section class="card card--front">
    <div class="brand">
      <span class="brand__name">Lumarra</span>
      <span class="brand__place">BEVERLY HILLS</span>
    </div>
  </section>

  <section class="card card--back">
    <div class="brand">
      <span class="brand__name">Lumarra</span>
      <span class="brand__place">BEVERLY HILLS</span>
    </div>
    <div class="person">
      <div class="person__row">
        <span class="person__name">NORA WHITFIELD</span>
        <span class="rule"></span>
      </div>
      <p class="person__role">Makeup Artist</p>
      <div class="rule rule--full"></div>
      <ul class="contact">
        <li><span class="contact__label">A:</span>6128 N.Corbel Ridge Blvd Beverly Hills , CA 90210</li>
        <li><span class="contact__label">E:</span><span class="contact__item">info@lumarrastudio-example.com</span><span class="contact__label">T:</span><span class="contact__item">555-014-2260</span><span class="contact__label">W:</span>lumarrastudio-example.com</li>
      </ul>
    </div>
  </section>
</body>
</html>
```